We are looking for a clean new looking business card.

We would like a new, clean, and modern type business card with our updated contact information. We are a small a plumbing and heating and gasfitting company who offer 24 hr emergency service as well.
We feel our logo looks best on a white background.
Our current cards are outdated, both the design and the information.

Industry/Entity Type

Plumbing and heating

Contact Information for Business Card

Logo, Name, Title, Phone#, Email, Website, "24/7 Emergency Service"

Colors
0054AA
0677BA
7BADD7
CADEEF
E8F1F8

```html
<!DOCTYPE html>
<html lang="en">
<head>
<meta charset="UTF-8">
<title>Clearbrook Business Card</title>
<link href="https://fonts.googleapis.com/css2?family=Poppins:wght@400;500;600&family=Fira+Sans:wght@600&family=Krona+One&display=swap" rel="stylesheet">
<style>
  :root {
    --navy: #0054AA;
    --blue: #0677BA;
    --sky: #7BADD7;
    --pale: #CADEEF;
    --mist: #E8F1F8;
    --ink: #333333;
    --stage: #262626;
    --white: #ffffff;
  }
  * { margin: 0; padding: 0; box-sizing: border-box; }
  html, body { width: 1075px; height: 1200px; overflow: hidden; background: var(--stage); }
  .canvas { position: relative; width: 1075px; height: 1200px; }

  .card {
    position: absolute;
    left: 206px;
    width: 663px;
    height: 395px;
    overflow: hidden;
    box-shadow: 3px 3px 0 rgba(0,0,0,0.55);
  }
  .card--front {
    top: 187px;
    background: linear-gradient(200deg, #9bd0e8 0%, #4fb0da 35%, #1f93c8 60%, #0a6fb0 100%);
    color: var(--white);
  }
  .card--back {
    top: 637px;
    background: linear-gradient(160deg, #e9e9e9 0%, #fbfbfb 45%, #f1f1f1 100%);
  }

  .decor {
    position: absolute;
    right: 0; top: 0;
    width: 360px; height: 395px;
  }
  .card--front .decor {
    background: radial-gradient(ellipse at 70% 45%, rgba(123,173,215,0.55) 0%, rgba(123,173,215,0.2) 55%, rgba(123,173,215,0) 80%);
  }
  .card--back .decor {
    background: radial-gradient(ellipse at 65% 50%, rgba(202,222,239,0.7) 0%, rgba(232,241,248,0.4) 55%, rgba(232,241,248,0) 80%);
  }

  .brand { position: absolute; text-align: center; }
  .brand__dot { display: block; margin: 0 auto; border-radius: 50%; }
  .brand__name {
    font-family: "Fira Sans", sans-serif;
    font-weight: 600;
    line-height: 1;
  }
  .brand__tagline {
    font-family: "Poppins", sans-serif;
    font-weight: 600;
    text-transform: uppercase;
    white-space: nowrap;
  }

  .card--front .brand { left: 22px; top: 42px; width: 300px; }
  .card--front .brand__dot { width: 50px; height: 50px; background: var(--white); }
  .card--front .brand__name { font-size: 46px; letter-spacing: 2.5px; margin-top: 20px; color: var(--white); }
  .card--front .brand__tagline { font-size: 9.5px; letter-spacing: 2.6px; margin-top: 6px; color: var(--white); }

  .person { position: absolute; left: 34px; top: 218px; font-family: "Poppins", sans-serif; }
  .person__name { font-size: 25px; font-weight: 600; line-height: 1.1; }
  .person__role { font-size: 18px; font-weight: 400; line-height: 1.1; }

  .contacts { position: absolute; left: 35px; top: 296px; list-style: none; font-family: "Poppins", sans-serif; font-size: 18px; }
  .contacts li { display: flex; align-items: center; height: 23.5px; }
  .contacts svg { width: 18px; height: 18px; margin-right: 5px; flex: none; }

  .card--back .brand { left: 0; right: 0; top: 95px; }
  .card--back .brand__dot { width: 84px; height: 84px; background: var(--blue); }
  .card--back .brand__name { font-size: 62px; letter-spacing: 4px; margin-top: 20px; color: var(--blue); }
  .card--back .brand__tagline { font-size: 15px; letter-spacing: 4.6px; margin-top: 8px; color: var(--ink); }
  .emergency {
    position: absolute; left: 0; right: 0; top: 322px;
    text-align: center;
    font-family: "Krona One", sans-serif;
    font-size: 22px;
    letter-spacing: 1px;
    color: #1590C8;
  }
</style>
</head>
<body>
<div class="canvas">

  <section class="card card--front">
    <div class="decor" role="img" aria-label="Large faint brand symbol pattern in light blue tones"></div>
    <div class="brand">
      <span class="brand__dot"></span>
      <div class="brand__name">clearbrook</div>
      <div class="brand__tagline">Plumbing · Heating · Gasfitting</div>
    </div>
    <div class="person">
      <div class="person__name">Daniel Hartley</div>
      <div class="person__role">Managing Director</div>
    </div>
    <ul class="contacts">
      <li>
        <svg viewBox="0 0 24 24" fill="none" stroke="currentColor" stroke-width="2.2" stroke-linejoin="round"><path d="M5 3h4l2 5-2.5 1.5a11 11 0 0 0 6 6L16 13l5 2v4a2 2 0 0 1-2 2A16 16 0 0 1 3 5a2 2 0 0 1 2-2z"/></svg>
        055-270 318 642
      </li>
      <li>
        <svg viewBox="0 0 24 24" fill="currentColor"><path d="M2 5h20v14H2z"/><path d="M2 5l10 8 10-8" fill="none" stroke="#1580bb" stroke-width="2"/></svg>
        hello@clearbrook.com
      </li>
      <li>
        <svg viewBox="0 0 24 24" fill="none" stroke="currentColor" stroke-width="1.8"><circle cx="12" cy="12" r="9.5"/><ellipse cx="12" cy="12" rx="4" ry="9.5"/><path d="M2.5 12h19M4 7h16M4 17h16"/></svg>
        www.clearbrookpro.com
      </li>
    </ul>
  </section>

  <section class="card card--back">
    <div class="decor" role="img" aria-label="Large faint brand symbol pattern in pale blue tones"></div>
    <div class="brand">
      <span class="brand__dot"></span>
      <div class="brand__name">clearbrook</div>
      <div class="brand__tagline">Plumbing · Heating · Gasfitting</div>
    </div>
    <div class="emergency">24/7 Emergency Service</div>
  </section>

</div>
</body>
</html>
```